Flyer für Vermieter von Monteursunterkünften
Zielgruppe
Guten Tag,
wir sind eine Fima, die Monteursunterkünfte vermietet. Wir vermieten möblierte Wohnungen auf Zeit. Man kann diese buchen ab 5 Tagen bis hin zu mehreren Monaten. Sie sind für Monteure, Handwerker oder Zeitarbeiter geeignet. Die Website dient lediglich zur Inspiration für Design und Farben. Auf der Website sprechen wir eine andere Zielgruppe an.
Mit den Flyern möchten wir Handwerksbetriebe oder auch Handwerker direkt ansprechen, welche auf der Suche nach einer günstigen und möblierten Unterkunft auf Zeit sind.
Es sollen beide Logos von der QT Dwelling und der RuhOrt17 verwendet werden.
Aufgabenstellung
Sie sind auf der Suche nach einer günstigen und komfortablen Unterkunft für Ihre Mitarbeiter? Dann sind Sie bei uns genau richtig!
BUCHEN Sie JETZT SCHNELL und EINFACH: 01629 581706
• Moderne und komfortable Wohnungen
• TV und Kühlschränke auf jedem Zimmer
• Voll ausgestattete Küche
• Immer mit Balkon oder Terrasse
• Kostenloses schnelles W-Lan
• Gute Parkmöglichkeiten
• Willkommenspaket
Überzeugen Sie sich selbst von unserem Angebot und buchen Sie noch heute eines unserer Monteurzimmer! Wir freuen uns auf Ihren Besuch.

```html
<!DOCTYPE html>
<html lang="de">
<head>
<meta charset="utf-8">
<title>Monteurzimmer Flyer – QT Dwelling &amp; RuhOrt17</title>
<link rel="stylesheet" href="https://fonts.googleapis.com/css2?family=Open+Sans:ital,wght@0,700;1,800&display=swap">
<style>
  :root {
    --bg: #5ce0e6;
    --ink: #0d0d0d;
  }
  html, body {
    margin: 0;
    padding: 0;
    overflow: hidden;
  }
  body {
    width: 848px;
    height: 1200px;
  }
  .flyer {
    position: relative;
    width: 848px;
    height: 1200px;
    background: var(--bg);
    color: var(--ink);
    font-family: "Open Sans", Arial, sans-serif;
    overflow: hidden;
  }
  .headline {
    position: absolute;
    left: 14px;
    width: 820px;
    top: 36px;
    margin: 0;
    font-size: 35.5px;
    line-height: 51px;
    font-weight: 700;
    text-align: center;
  }
  .features {
    position: absolute;
    left: 14px;
    width: 820px;
    top: 305px;
    margin: 0;
    padding: 0;
    list-style: none;
    font-size: 33px;
    line-height: 47.4px;
    font-weight: 700;
    text-align: center;
  }
  .closing {
    position: absolute;
    left: 10px;
    width: 800px;
    top: 680px;
    margin: 0;
    font-size: 33.5px;
    line-height: 47px;
    font-weight: 700;
    text-align: center;
  }
  .booking {
    position: absolute;
    left: 24px;
    width: 800px;
    top: 909px;
    margin: 0;
    font-size: 29px;
    line-height: 41px;
    font-weight: 800;
    font-style: italic;
    text-align: center;
  }
  .brand-primary {
    position: absolute;
    left: 18px;
    top: 1104px;
    font-size: 22px;
    font-weight: 700;
    letter-spacing: 1px;
  }
  .brand-partner {
    position: absolute;
    left: 510px;
    top: 1000px;
    font-size: 34px;
    font-weight: 700;
  }
  .townscape {
    position: absolute;
    left: 186px;
    top: 1058px;
    width: 432px;
    height: 134px;
    background: linear-gradient(180deg, #1a1a1a, #050505);
    border-radius: 6px 6px 0 0;
  }
</style>
</head>
<body>
  <main class="flyer">
    <h1 class="headline">Sie sind auf der Suche nach einer günstigen<br>und komfortablen Unterkunft für Ihre<br>Mitarbeiter? Dann sind Sie bei uns genau<br>richtig!</h1>

    <ul class="features">
      <li>• Moderne und komfortable Wohnungen</li>
      <li>• TV und Kühlschränke auf jedem Zimmer</li>
      <li>• Voll ausgestattete Küche</li>
      <li>• Immer mit Balkon oder Terrasse</li>
      <li>• Kostenloses schnelles W-Lan</li>
      <li>• Gute Parkmöglichkeiten</li>
      <li>• Willkommenspaket</li>
    </ul>

    <p class="closing">Überzeugen Sie sich selbst von unserem<br>Angebot und buchen Sie noch heute eines<br>unserer Monteurzimmer! Wir freuen uns auf<br>Ihren Besuch.</p>

    <p class="booking">BUCHEN Sie JETZT SCHNELL und EINFACH: 01629<br>581706</p>

    <div class="brand-primary">QT Dwelling</div>

    <div class="brand-partner">RuhOrt17</div>

    <div class="townscape" role="img" aria-label="Silhouette einer Häuserzeile mit Giebeln und Fenstern"></div>
  </main>
</body>
</html>
```